Webdesign Handwerkerportal
Zielgruppe
Wir bieten eine Informationsplattform für Handwerkerbetriebe an.
Aufgabenstellung
wir benötigen ein Webdesign für unsere Werbsite.
Es handelt sich um eine Informationsplattform für Meisternetz jeder Branche. Hier können ausschließlich registrierte Firmen und Meisternetz Informationen austauschen.
Eine Menüleiste kann links oder am oberen Rand angebracht werden.
Das Design muss Seriösität vermitteln.
Kenntniss und Verständnis für Meisternetz und deren Bedürfnisse sollte als Aussage im Design wie auch Vertrauen vermittelt werden.
z. B. 1 Auto / Pritsche, einen Kurvano einen Meisternetz im Blaumann, einen Vorarbeiter im grauen Kittel, evtl. mit Helm. Für andere Vorschläge sind wir offen.
in diese Richtung ( ähnlich dem alten Zelvo Handshake, welcher aufeinanderzugehen und Vertrautheit vermittelt ) könnten wir uns vorstellen.

```html
<!DOCTYPE html>
<html lang="de">
<head>
<meta charset="utf-8">
<title>Meisternetz – Informationsplattform für Handwerksbetriebe</title>
<link href="https://fonts.googleapis.com/css2?family=Open+Sans:ital,wght@0,300;0,400;0,600;0,700;1,400&display=swap" rel="stylesheet">
<style>
  :root {
    --blue: #2560a8;
    --blue-dark: #1f4f94;
    --topbar: #d9d9d9;
    --nav-text: #b9bcc0;
    --text: #555a5e;
    --text-light: #8a8e92;
    --card: #f2f2f2;
    --track: #e3e3e3;
    --footer: #595d60;
    --white: #ffffff;
  }
  * { margin: 0; padding: 0; box-sizing: border-box; }
  html, body { width: 998px; height: 1200px; overflow: hidden; }
  body { position: relative; background: var(--white); font-family: "Open Sans", Arial, sans-serif; color: var(--text); }
  .abs { position: absolute; }

  .topbar { left: 0; top: 0; width: 998px; height: 19px; background: var(--topbar); }
  .topbar-links { right: 220px; top: 5px; font-size: 8px; color: var(--white); }
  .topbar-links span { margin-left: 8px; }

  .brand { left: 219px; top: 40px; display: flex; align-items: center; gap: 7px; }
  .brand-mark { width: 12px; height: 12px; background: var(--blue); }
  .brand-name { font-size: 18px; font-weight: 600; color: var(--blue); line-height: 1; }
  .brand-tagline { left: 219px; top: 60px; font-size: 9px; color: var(--text-light); }

  .main-nav { left: 0; top: 19px; width: 998px; height: 76px; }
  .nav-item { position: absolute; top: 32px; font-size: 11.3px; color: var(--nav-text); line-height: 1; }
  .nav-item.is-active { top: 0; height: 76px; padding: 32px 7px 0; background: var(--blue); color: var(--white); }

  .hero { left: 0; top: 95px; width: 998px; height: 308px;
    background: linear-gradient(90deg, #e9e2d9 0%, #d9c8b4 22%, #e6e3df 45%, #b8cbe0 62%, #a8bcd4 78%, #d7dde4 100%); }
  .hero-title { left: 217px; top: 223px; font-size: 30px; font-weight: 600; color: var(--blue-dark); letter-spacing: -0.5px; line-height: 1; }
  .hero-subtitle { left: 217px; top: 259px; font-size: 22px; font-weight: 300; color: #5a5a5a; line-height: 1; }
  .btn { position: absolute; top: 304px; width: 142px; height: 32px; font-size: 11.5px; text-align: center; line-height: 30px; }
  .btn-primary { left: 220px; background: var(--blue); color: var(--white); font-weight: 600; line-height: 32px; }
  .btn-outline { left: 366px; border: 1.5px solid var(--blue); color: var(--blue); }

  .features { left: 0; top: 403px; width: 998px; height: 287px; background: var(--blue); color: var(--white); }
  .features-title { position: absolute; left: 0; top: 23px; width: 1002px; text-align: center; font-size: 17px; font-weight: 400; }
  .feature { position: absolute; top: 68px; width: 180px; text-align: center; }
  .feature svg { display: block; margin: 0 auto; width: 60px; height: 60px; }
  .feature h3 { margin-top: 13px; font-size: 11px; font-weight: 700; letter-spacing: 0.2px; }
  .feature p { margin-top: 4px; font-size: 10px; line-height: 13.7px; }

  .intro-title { left: 219px; top: 740px; font-size: 21px; font-weight: 700; color: var(--blue); line-height: 1.2; }
  .intro-subtitle { left: 219px; top: 766px; font-size: 15px; font-weight: 400; color: var(--text); }
  .intro-text { left: 219px; top: 803px; width: 340px; font-size: 10px; line-height: 14.3px; }

  .worker-photo { left: 140px; top: 906px; width: 207px; height: 250px;
    background: linear-gradient(180deg, #f6f6f7 0%, #e9edf3 55%, #c9d6ea 100%); }
  .testimonial { right: 459px; top: 996px; width: 262px; text-align: right; font-size: 11.3px; font-style: italic; line-height: 17.8px; color: var(--text); }
  .testimonial cite { display: block; margin-top: 3px; font-size: 8.3px; font-style: normal; color: var(--blue); line-height: 1.4; }

  .news-title { left: 599px; top: 744px; font-size: 15.5px; font-weight: 700; color: var(--blue); letter-spacing: 0.3px; }
  .news-subtitle { left: 599px; top: 764px; font-size: 8.5px; color: var(--text); }
  .news-card { position: absolute; left: 600px; width: 168px; height: 97px; background: var(--card); padding: 11px 13px; }
  .news-card h4 { font-size: 9.5px; font-weight: 700; color: var(--blue); line-height: 1.2; }
  .news-card time { display: block; font-size: 8.3px; color: var(--text-light); line-height: 1.35; }
  .news-card p { margin-top: 3px; font-size: 8.3px; color: var(--text-light); line-height: 12px; }
  .scroll-track { left: 772px; top: 797px; width: 6px; height: 301px; background: var(--track); }
  .scroll-thumb { left: 772px; top: 797px; width: 6px; height: 139px; background: var(--blue); }
  .btn-more { left: 600px; top: 1111px; width: 178px; height: 25px; background: var(--blue); color: var(--white); font-size: 9px; font-weight: 700; text-align: center; line-height: 25px; }

  .site-footer { left: 0; top: 1156px; width: 998px; height: 44px; background: var(--footer); }
  .footer-links { position: absolute; left: 220px; top: 15px; font-size: 8.5px; color: var(--white); }
  .footer-links .sep { margin: 0 5px; }
  .social { position: absolute; left: 720px; top: 12px; display: flex; gap: 2.5px; }
  .social span { width: 12.5px; height: 12.5px; background: var(--white); }
</style>
</head>
<body>
  <header>
    <div class="abs topbar"></div>
    <div class="abs topbar-links"><span>LOGIN</span><span>REGISTRIEREN</span></div>
    <div class="abs brand"><span class="brand-mark"></span><span class="brand-name">Meisternetz</span></div>
    <div class="abs brand-tagline">INFOPLATTFORM FÜR BETRIEBE</div>
    <nav class="abs main-nav">
      <span class="nav-item" style="left:436px">INFORMATIONEN</span>
      <span class="nav-item is-active" style="left:539px;width:89px">HANDWERKER</span>
      <span class="nav-item" style="left:639px">UNTERNEHMEN</span>
      <span class="nav-item" style="left:738px">FORUM</span>
    </nav>
  </header>

  <section>
    <div class="abs hero" role="img" aria-label="Foto: Handwerker mit Schutzhelm, Werkzeuggürtel und Hammer auf einer Baustelle"></div>
    <h1 class="abs hero-title">DAS HANDWERKERPORTAL</h1>
    <div class="abs hero-subtitle">DOLOR SIT AMET</div>
    <div class="btn btn-primary">JETZT ANMELDEN</div>
    <div class="btn btn-outline">MEHR ERFAHREN</div>
  </section>

  <section class="abs features">
    <h2 class="features-title">AENEAN MASSA, CUM SOCIIS NATOQUE</h2>
    <div class="feature" style="left:219px">
      <svg viewBox="0 0 60 60" aria-hidden="true">
        <path d="M6 38 C6 20 18 9 31 9 C44 9 52 20 52 33 L58 36 C55 44 48 47 38 47 C26 47 14 44 8 42 Z" fill="#fff"/>
        <path d="M29 12 C38 12 44 20 46 30" stroke="var(--blue)" stroke-width="2.5" fill="none"/>
        <path d="M24 13 C32 14 37 21 39 30" stroke="var(--blue)" stroke-width="2.5" fill="none"/>
        <path d="M10 41 C20 45 34 46 46 43" stroke="var(--blue)" stroke-width="2" fill="none"/>
      </svg>
      <h3>LOREM IPSUM DOLOR</h3>
      <p>Lorem ipsum dolor sit amet, consectetuer adipiscing elit. Aenean commodo ligula eget dolor. Aenean massa. Cum sociis natoque penatibus et magnis dis parturient montes.</p>
    </div>
    <div class="feature" style="left:408px">
      <svg viewBox="0 0 60 60" aria-hidden="true">
        <path d="M30 4 L36 9 L44 8 L46 15 L53 19 L51 27 L55 33 L50 39 L50 47 L42 48 L37 54 L30 51 L23 54 L18 48 L10 47 L10 39 L5 33 L9 27 L7 19 L14 15 L16 8 L24 9 Z" fill="#fff"/>
        <circle cx="30" cy="30" r="15" fill="none" stroke="var(--blue)" stroke-width="3.5"/>
        <path d="M23 30 L28 35 L38 24" fill="none" stroke="var(--blue)" stroke-width="4" stroke-linecap="round" stroke-linejoin="round"/>
      </svg>
      <h3>LOREM IPSUM DOLOR</h3>
      <p>Lorem ipsum dolor sit amet, consectetuer adipiscing elit. Aenean commodo ligula eget dolor. Aenean massa. Cum sociis natoque penatibus et magnis dis parturient montes.</p>
    </div>
    <div class="feature" style="left:601px">
      <svg viewBox="0 0 60 60" aria-hidden="true">
        <path d="M14 4 C8 5 4 10 5 16 L11 12 L16 15 L16 21 L10 24 C15 28 21 27 24 23 L50 50 C52 53 57 52 57 48 L30 20 C33 13 27 3 14 4 Z" fill="#fff"/>
        <path d="M34 6 L48 6 L56 14 L52 18 L46 14 L14 50 C11 55 5 53 6 48 L39 15 L34 10 Z" fill="#fff"/>
        <circle cx="53" cy="49" r="2.2" fill="var(--blue)"/>
      </svg>
      <h3>LOREM IPSUM DOLOR</h3>
      <p>Lorem ipsum dolor sit amet, consectetuer adipiscing elit. Aenean commodo ligula eget dolor. Aenean massa. Cum sociis natoque penatibus et magnis dis parturient montes.</p>
    </div>
  </section>

  <main>
    <h2 class="abs intro-title">DAS HANDWERKERPORTAL</h2>
    <div class="abs intro-subtitle">ALLES RUND UM’S HANDWERK</div>
    <p class="abs intro-text">Lorem ipsum dolor sit amet, consectetuer adipiscing elit. Aenean commodo ligula eget dolor. Aenean massa. Cum sociis natoque penatibus et magnis dis parturient montes, nascetur ridiculus mus. Donec quam felis, ultricies nec, pellentesque eu, pretium quis, sem. Nulla consequat massa quis enim. Donec pede justo, fringilla vel, aliquet nec, vulputate eget, arcu. In enim justo, rhoncus ut, imperdiet a, venenatis vitae, justo.</p>
    <div class="abs worker-photo" role="img" aria-label="Foto: lächelnder Handwerker im blauen Blaumann mit rotem Helm und Kabelrolle"></div>
    <blockquote class="abs testimonial">„Aliquam lorem ante, dapibus in, viverra quis, feugiat a, tellus. Phasellus viverra nulla ut metus varius laoreet. Quisque rutrum. Aenean imperdiet. Etiam ultricies nisi vel augue. “
      <cite>- JONAS BRENNER</cite>
    </blockquote>
  </main>

  <aside>
    <h2 class="abs news-title">NEUIGKEITEN</h2>
    <div class="abs news-subtitle">IMMER INFORMIERT</div>
    <article class="news-card" style="top:797px">
      <h4>LOREM IPSUM DOLOR</h4><time>14. MAI 2014</time>
      <p>Lorem ipsum dolor sit amet, consectetuer adipiscing elit. Aenean commodo ligula eget dolor.</p>
    </article>
    <article class="news-card" style="top:899px">
      <h4>LOREM IPSUM DOLOR</h4><time>14. MAI 2014</time>
      <p>Lorem ipsum dolor sit amet, consectetuer adipiscing elit. Aenean commodo ligula eget dolor.</p>
    </article>
    <article class="news-card" style="top:1001px">
      <h4>LOREM IPSUM DOLOR</h4><time>14. MAI 2014</time>
      <p>Lorem ipsum dolor sit amet, consectetuer adipiscing elit. Aenean commodo ligula eget dolor.</p>
    </article>
    <div class="abs scroll-track"></div>
    <div class="abs scroll-thumb"></div>
    <div class="abs btn-more">MEHR</div>
  </aside>

  <footer class="abs site-footer">
    <div class="footer-links">KONTAKT<span class="sep">|</span>IMPRESSUM</div>
    <div class="social" aria-label="Soziale Netzwerke"><span></span><span></span><span></span><span></span></div>
  </footer>
</body>
</html>
```